Harlow Stonefield Civil Construction website design

We want a Bold website to promote our Heavy Civil Construction company, We would like an organic / tangible feel to the site. The pictures will be over saturated so they pop. We need to be able to easliy upload new projects and pictures on a regular basis.
Home page will have a full screen width image, "home page image" with silhouette and logo. It will also have about us area and picture
Page 2 will be Project Gallery with pictures in project folders
Page 3 will be an employment application form and submission
Page 4 will be Contact Us
Target Market(s)
Construction indusrty
Industry/Entity Type
Contractor
Coding
Coded - Design and coding required
Number of Pages Required
4 page
Font styles to use
Other font styles liked:
- Hypatia Sans Pro Light
Look and feel

```html
<!DOCTYPE html>
<html lang="en">
<head>
<meta charset="utf-8">
<title>Harlow Stonefield Civil Construction</title>
<link href="https://fonts.googleapis.com/css2?family=Lato:wght@300;400;700&display=swap" rel="stylesheet">
<style>
:root{
  --navy:#2b3a8f;
  --navy-dark:#1f2c73;
  --navy-deep:#18225c;
  --white:#ffffff;
  --text:#555a66;
  --heading:#3a3f4a;
  --band-grey:#8f9196;
  --light:#eeeff1;
  --link:#2b3a8f;
}
*{box-sizing:border-box;margin:0;padding:0}
html,body{width:1200px;height:2988px;overflow:hidden}
body{font-family:"Lato",Arial,sans-serif;color:var(--text);background:var(--white);position:relative}
.abs{position:absolute}

/* header */
.site-header{left:0;top:0;width:1200px;height:84px;background:var(--white)}
.brand{left:72px;top:14px;display:flex;align-items:center;gap:14px}
.brand-mark{width:46px;height:46px;background:var(--navy)}
.brand-name{font-size:22px;font-weight:700;color:var(--navy);line-height:1.1;letter-spacing:.5px;text-transform:uppercase}
.contact-strip{right:72px;top:26px;display:flex;gap:28px;font-size:15px;color:var(--text);align-items:center}
.contact-strip span{display:flex;align-items:center;gap:8px}

/* nav */
.main-nav{left:0;top:84px;width:1200px;height:40px;background:var(--navy)}
.main-nav ul{list-style:none;display:flex;margin-left:164px;height:40px}
.main-nav li{color:var(--white);font-size:15px;letter-spacing:1px;padding:0 24px;line-height:40px;text-transform:uppercase}
.main-nav li.active{background:#5866b0}

/* hero */
.hero{left:0;top:124px;width:1200px;height:628px;background:linear-gradient(180deg,#c8d3dc 0%,#dfe4e6 30%,#a9a89a 55%,#6f7a55 75%,#556040 100%)}
.hero-title{left:0;top:340px;width:1200px;text-align:center;color:var(--white);font-weight:300;text-transform:uppercase}
.hero-title .line1{font-size:68px;letter-spacing:3px;display:block}
.hero-title .line2{font-size:42px;letter-spacing:10px;display:block;margin-top:6px}
.hero-square{left:540px;top:250px;width:120px;height:80px;border:4px solid rgba(255,255,255,.85)}
.dots{left:0;top:662px;width:1200px;display:flex;justify-content:center;gap:10px}
.dots i{width:12px;height:12px;border-radius:50%;background:rgba(255,255,255,.6);display:block}
.dots i.on{background:var(--navy)}

/* about */
.about{left:0;top:752px;width:1200px;height:340px;background:linear-gradient(180deg,#f4f4f5,#e6e7e9)}
.about-photo{left:72px;top:794px;width:330px;height:210px;background:linear-gradient(180deg,#8aa0b8,#7d8a6a)}
.section-title{font-weight:300;text-transform:uppercase;color:var(--heading);font-size:36px;letter-spacing:.5px}
.body-copy{font-size:15px;line-height:26px}
.btn{background:var(--navy);color:var(--white);font-size:14px;letter-spacing:1px;text-transform:uppercase;padding:0 24px;height:40px;line-height:40px;display:inline-block}

/* heavy civil */
.civil{left:0;top:1080px;width:1200px;height:520px;background:var(--band-grey);clip-path:polygon(0 0,50% 50px,100% 0,100% 100%,50% calc(100% - 50px),0 100%)}
.civil .section-title{color:var(--white)}
.civil-copy{color:#f1f2f4}
.civil-photo{left:612px;top:1180px;width:524px;height:330px;background:linear-gradient(180deg,#b7c7d4 0%,#9a8f78 45%,#6c7752 100%)}

/* gallery */
.gallery{left:0;top:1590px;width:1200px;height:620px;background:linear-gradient(180deg,#ffffff,#e8e9eb);clip-path:polygon(0 0,100% 0,100% calc(100% - 50px),50% 100%,0 calc(100% - 50px))}
.gallery-title{left:0;top:1624px;width:1200px;text-align:center}
.card{top:1700px;width:330px}
.card-photo{width:330px;height:186px;background:linear-gradient(180deg,#a7b9c8,#8e7c62 60%,#6b744e)}
.card h3{margin-top:22px;font-size:22px;font-weight:400;color:var(--link);text-transform:uppercase;letter-spacing:.5px}
.card p{margin-top:8px;font-size:14px;line-height:22px}
.arrow{top:1860px}

/* employment */
.employ-photo{left:72px;top:2248px;width:516px;height:334px;background:linear-gradient(135deg,#e9e6df,#c7c1b4 60%,#a9a394)}

/* footer */
.site-footer{left:0;top:2656px;width:1200px;height:288px;background:var(--navy)}
.footer-col{top:2690px;color:#d7dbf0;font-size:14px}
.footer-col h4{font-size:16px;font-weight:400;letter-spacing:1px;text-transform:uppercase;color:var(--white);margin-bottom:18px}
.footer-col li{list-style:none;line-height:28px;display:flex;align-items:center;gap:10px}
.sq{width:14px;height:14px;background:rgba(255,255,255,.55);display:inline-block}
.copyright{left:0;top:2944px;width:1200px;height:44px;background:var(--navy-deep);color:#aab0d4;font-size:12px;text-align:center;line-height:44px}
</style>
</head>
<body>

<header class="site-header abs">
  <div class="brand abs">
    <div class="brand-mark"></div>
    <div class="brand-name">Harlow Stonefield<br>Civil Construction</div>
  </div>
  <div class="contact-strip abs">
    <span><svg width="14" height="14" viewBox="0 0 24 24"><path fill="#2b3a8f" d="M6.6 10.8a15 15 0 0 0 6.6 6.6l2.2-2.2c.3-.3.7-.4 1-.2 1.1.4 2.3.6 3.6.6.6 0 1 .4 1 1V20c0 .6-.4 1-1 1A17 17 0 0 1 3 4c0-.6.4-1 1-1h3.5c.6 0 1 .4 1 1 0 1.3.2 2.5.6 3.6.1.3 0 .7-.2 1z"/></svg>1-800-555-0147</span>
    <span><svg width="16" height="12" viewBox="0 0 16 12"><rect width="16" height="12" fill="#2b3a8f"/><path d="M0 0l8 6 8-6" stroke="#fff" fill="none" stroke-width="1.4"/></svg>info@harlowstonefield.com</span>
  </div>
</header>

<nav class="main-nav abs">
  <ul>
    <li class="active">Home</li>
    <li>About Us</li>
    <li>Project Gallery</li>
    <li>Employee Application</li>
    <li>Contact Us</li>
  </ul>
</nav>

<section class="hero abs" role="img" aria-label="Wide photo of a heavy civil construction site with earthworks and green erosion netting under a bright sky"></section>
<div class="hero-square abs"></div>
<h1 class="hero-title abs"><span class="line1">Harlow Stonefield</span><span class="line2">Civil Construction</span></h1>
<div class="dots abs"><i class="on"></i><i></i><i></i><i></i></div>

<section class="about abs"></section>
<div class="about-photo abs" role="img" aria-label="Photo of an excavator working on a project site"></div>
<h2 class="section-title abs" style="left:440px;top:786px">About Harlow Stonefield</h2>
<p class="body-copy abs" style="left:440px;top:836px;width:690px">Lorem ipsum dolor sit amet, consectetur adipiscing elit. Aenean posuere vitae leo sodales ege stas. Etiam fermentum tortor lacus, eget interdum urna volutpat id. Proin sagittis dapibus porta. Mauris nec orci non diam posuere aliquet a vel massa. Etiam tincidunt urna in dui eges tas, vel ornare enim scelerisque.</p>
<span class="btn abs" style="left:440px;top:964px">Read More</span>

<section class="civil abs"></section>
<h2 class="section-title abs" style="left:72px;top:1180px;color:#fff">Heavy Civil Construction</h2>
<p class="body-copy civil-copy abs" style="left:72px;top:1236px;width:500px">Lorem ipsum dolor sit amet, consectetur adipiscing elit. Aenean posuere vitae leo sodales egestas. Etiam fermentum tortor lacus, eget interdum urna volutpat id. Proin sagittis dapibus porta. Mauris nec orci non diam posuere aliquet a vel massa. Etiam tincidunt urna in dui egestas, vel ornare enim scelerisque. Morbi at mi interdum, rutrum elit vitae, auctor quam. Proin finibus eget lorem pharetra venenatis.</p>
<span class="btn abs" style="left:72px;top:1432px">Read More</span>
<div class="civil-photo abs" role="img" aria-label="Aerial photo of a large building site with cleared ground"></div>

<section class="gallery abs"></section>
<h2 class="section-title gallery-title abs">Project Gallery</h2>
<svg class="arrow abs" style="left:36px" width="16" height="28" viewBox="0 0 16 28"><path d="M14 2L3 14l11 12" stroke="#3a3f4a" stroke-width="3" fill="none"/></svg>
<svg class="arrow abs" style="left:1148px" width="16" height="28" viewBox="0 0 16 28"><path d="M2 2l11 12L2 26" stroke="#3a3f4a" stroke-width="3" fill="none"/></svg>

<article class="card abs" style="left:72px">
  <div class="card-photo" role="img" aria-label="Aerial photo of a road and site project"></div>
  <h3>Proin Sagittis Dapibus</h3>
  <p>Vivamus nec nulla tincidunt, porta nisl et, congue odio. Pellentesque risus massa, faucibus eu quam in, pulvinar ultricies tellus.</p>
</article>
<article class="card abs" style="left:436px">
  <div class="card-photo" role="img" aria-label="Aerial photo of a graded building pad"></div>
  <h3>Proin Sagittis Dapibus</h3>
  <p>Vivamus nec nulla tincidunt, porta nisl et, congue odio. Pellentesque risus massa, faucibus eu quam in, pulvinar ultricies tellus.</p>
</article>
<article class="card abs" style="left:800px">
  <div class="card-photo" role="img" aria-label="Aerial photo of a commercial site under construction"></div>
  <h3>Proin Sagittis Dapibus</h3>
  <p>Vivamus nec nulla tincidunt, porta nisl et, congue odio. Pellentesque risus massa, faucibus eu quam in, pulvinar ultricies tellus.</p>
</article>
<span class="btn abs" style="left:494px;top:2062px">View All Projects</span>

<div class="employ-photo abs" role="img" aria-label="Photo of a hand signing an application form with a pen"></div>
<h2 class="section-title abs" style="left:612px;top:2252px">Employee Application</h2>
<p class="body-copy abs" style="left:612px;top:2308px;width:520px">Lorem ipsum dolor sit amet, consectetur adipiscing elit. Aenean posuere vitae leo sodales egestas. Etiam fermentum tortor lacus, eget interdum urna volutpat id. Proin sagittis dapibus porta. Mauris nec orci non diam posuere aliquet a vel massa. Etiam tincidunt urna in dui egestas, vel ornare enim scelerisque. Morbi at mi interdum, rutrum elit vitae, auctor quam. Proin finibus eget lorem pharetra venenatis.</p>
<span class="btn abs" style="left:612px;top:2504px">Apply Now</span>

<footer class="site-footer abs"></footer>
<div class="abs" style="left:72px;top:2716px;display:flex;align-items:center;gap:12px">
  <div style="width:36px;height:36px;background:#fff"></div>
  <div style="color:#fff;font-size:17px;font-weight:700;text-transform:uppercase;line-height:1.1">Harlow Stonefield<br>Civil Construction</div>
</div>
<p class="abs" style="left:72px;top:2776px;width:240px;color:#d7dbf0;font-size:13px;line-height:21px">Duis aliquam nibh a dui iaculis viverra dui velit. Vivamus egestas risus in feugiat varius commodo tempor viverra egestas.</p>

<div class="footer-col abs" style="left:384px">
  <h4>Site Map</h4>
  <ul><li>Home</li><li>About us</li><li>Project Gallery</li><li>Employee Application</li><li>Contact us</li></ul>
</div>
<div class="footer-col abs" style="left:636px">
  <h4>Follow Us</h4>
  <ul>
    <li><i class="sq"></i>Community</li>
    <li><i class="sq"></i>News Feed</li>
    <li><i class="sq"></i>Network</li>
    <li><i class="sq"></i>Updates</li>
    <li><i class="sq"></i>Video Channel</li>
  </ul>
</div>
<div class="footer-col abs" style="left:904px">
  <h4>Contact Info</h4>
  <ul>
    <li style="align-items:flex-start;line-height:20px"><svg width="12" height="16" viewBox="0 0 12 16" style="margin-top:3px"><path d="M6 0a6 6 0 0 1 6 6c0 4-6 10-6 10S0 10 0 6a6 6 0 0 1 6-6z" fill="#d7dbf0"/><circle cx="6" cy="6" r="2" fill="#2b3a8f"/></svg><span>2450 Quarry Road<br>Suite 12, Riverton<br>TX 77000</span></li>
    <li><svg width="12" height="12" viewBox="0 0 24 24"><path fill="#d7dbf0" d="M6.6 10.8a15 15 0 0 0 6.6 6.6l2.2-2.2c.3-.3.7-.4 1-.2 1.1.4 2.3.6 3.6.6.6 0 1 .4 1 1V20c0 .6-.4 1-1 1A17 17 0 0 1 3 4c0-.6.4-1 1-1h3.5c.6 0 1 .4 1 1 0 1.3.2 2.5.6 3.6.1.3 0 .7-.2 1z"/></svg>1-800-555-0147</li>
    <li><svg width="14" height="10" viewBox="0 0 16 12"><rect width="16" height="12" fill="#d7dbf0"/><path d="M0 0l8 6 8-6" stroke="#2b3a8f" fill="none" stroke-width="1.4"/></svg>info@harlowstonefield.com</li>
  </ul>
</div>

<div class="copyright abs">Copyright © 2014 Harlow Stonefield All Rights Reserved</div>

</body>
</html>
```